Web redesign for Asian (IndoPak) based private equity firm

Redesign TLKventures.com.
New site to be done on Wordpress. No flash, responsive. Keep logo. Home page, news, team, portfolio, contact us. Portfolio will be case study based so we will have some next about an industry like infrastructure and then Have logos below. Use existing images and others from Indian stock photo sites (will pay for those so use placeholders). Home page should have news feed and video front and center. Images should have eye contact. Looking for clean and simple design .

Sites we like
http://www.dmvh.com- use of video highlight

Leafly.in
A magazine that I find very easy to read and scroll down
Allows for both text /photo and video

Target Market(s)

Private equity

Industry/Entity Type

Financial Service

Coding

Coded - Design and coding required

Number of Pages Required

5+ page

Font styles to use
Serif
Sans Serif

Colors
3377b5
85acd3

Requirements
Must have
• Responsive, video highlight, image use, existing logo, contact us, open page design . Use existing color
Nice to have
• Connect news story to content on page using tags. Pop over for team bios, custom font
Should not have
• Flash, no need for inline CSS on the content pages except absolutely necessary. No rigid content types

```html
<!DOCTYPE html>
<html lang="en">
<head>
<meta charset="utf-8">
<title>TLK Ventures – Home</title>
<link href="https://fonts.googleapis.com/css2?family=Open+Sans:wdth,wght@75,300;100,400;100,600&family=Lato:wght@700&family=Noto+Serif&display=swap" rel="stylesheet">
<style>
:root{
  --brand:#1f3f8f;
  --link:#2ea3f2;
  --text:#333;
  --muted:#666;
  --rule:#e2e2e2;
  --footer-bg:#222;
  --footer-text:#777;
  --white:#fff;
}
*{margin:0;padding:0;box-sizing:border-box}
html,body{width:999px;height:1200px;overflow:hidden;background:var(--white)}
body{position:relative;font-family:"Open Sans",sans-serif;color:var(--text)}
a{text-decoration:none;color:inherit}

.site-header{position:absolute;top:0;left:0;width:999px;height:59px;background:var(--white);box-shadow:0 1px 0 rgba(0,0,0,.08)}
.brand{position:absolute;left:102px;top:14px;display:flex;align-items:center;gap:8px;font-family:"Noto Serif",serif;font-size:20px;color:var(--brand)}
.brand-mark{width:12px;height:12px;background:var(--brand)}
.main-nav{position:absolute;right:99px;top:22px;display:flex;gap:18px;font-family:"Lato",sans-serif;font-weight:700;font-size:12px;color:#111}
.main-nav .current{color:var(--link)}

.hero{position:absolute;top:59px;left:0;width:999px;height:269px;
  background:linear-gradient(90deg,#6f777c 0%,#7f8a94 30%,#9aa1a5 60%,#b9bcbe 100%)}
.hero-title{position:absolute;right:100px;top:52px;text-align:right;color:var(--white);font-weight:400}
.hero-title .big{font-size:80px;line-height:84px;display:block;font-weight:400}
.hero-title .small{font-size:64px;line-height:70px;display:block;font-weight:300;font-stretch:75%}

.sidebar{position:absolute;left:100px;top:386px;width:144px}
.sidebar h3{font-weight:400;font-size:14px;color:#222;margin-bottom:6px}
.video-thumb{width:144px;height:81px;background:linear-gradient(135deg,#7a1c2a,#c23a3a 50%,#2a2a4a)}
.sidebar p,.sidebar li{font-size:10.5px;line-height:17.7px;color:var(--muted)}
.sidebar p{margin-top:5px}
.recent{margin-top:34px}
.recent ul{list-style:none}
.recent li{margin-bottom:5px}
.sidebar-rule{position:absolute;left:266px;top:389px;width:1px;height:388px;background:var(--rule)}

.post{position:absolute;left:311px;width:589px}
.post h2{font-weight:600;font-size:20px;line-height:28px;color:#333}
.post .meta{font-size:10.5px;color:var(--muted);margin-top:8px;margin-bottom:6px}
.post .photo{width:589px;height:161px}
.post .excerpt{font-size:10.5px;line-height:17.7px;color:var(--muted);margin-top:6px;max-width:578px}
.post .more{display:block;font-size:10.5px;line-height:17.7px;color:var(--link);margin-top:2px}
.post hr{border:0;border-top:1px solid var(--rule);margin-top:14px}
.post-one{top:413px}
.post-one .photo{background:linear-gradient(90deg,#1f3f96 0%,#1f3f96 68%,#8a7262 80%,#4f5560 100%)}
.post-two{top:780px}
.post-two .photo{background:linear-gradient(90deg,#8d8a82,#c9c6c0 40%,#b2474e 55%,#d8d8d8 75%,#6d6a62)}

.site-footer{position:absolute;left:0;top:1143px;width:999px;height:57px;background:var(--footer-bg);padding:13px 100px 0}
.site-footer p{font-size:10.5px;line-height:17.7px;color:var(--footer-text)}
</style>
</head>
<body>
<header class="site-header">
  <a class="brand" href="#"><span class="brand-mark"></span>tlk ventures</a>
  <nav class="main-nav">
    <a class="current" href="#">Home</a>
    <a href="#">News</a>
    <a href="#">Team</a>
    <a href="#">Portfolio</a>
    <a href="#">Contact Us</a>
  </nav>
</header>

<section class="hero" role="img" aria-label="Banner photo of a globe showing the Americas on a grey background">
  <h1 class="hero-title"><span class="big">Evolve:</span><span class="small">Inspire</span></h1>
</section>

<aside class="sidebar">
  <h3>Videos</h3>
  <div class="video-thumb" role="img" aria-label="Video still of a stage conversation at a business forum"></div>
  <p>Arun Mehta in conversation with Meridian TV's Rohan Kapoor at City Tech Institute sponsored Global Business Forum - October 16, 2015</p>
  <div class="recent">
    <h3>Recent</h3>
    <ul>
      <li>Exclusive Interview of Mr. Arun Mehta in Asia Growth Review (AGR) magazine</li>
      <li>Vikram Thomas shares Pre-Budget views</li>
    </ul>
  </div>
</aside>
<div class="sidebar-rule"></div>

<article class="post post-one">
  <h2>Exclusive Interview of Mr. Arun Mehta in Asia Growth Review (AGR) magazine</h2>
  <div class="meta">Feb, 2017 | News and Events</div>
  <div class="photo" role="img" aria-label="Magazine feature banner on blue with a portrait of the interviewee"></div>
  <p class="excerpt">Arun Mehta is the CEO of TLK Ventures Partners, one of India's largest Private Equity (PE) funds with a primary focus on India and the Southeast Asia markets.</p>
  <a class="more" href="#">Continue reading &gt;&gt;</a>
  <hr>
</article>

<article class="post post-two">
  <h2>Vikram Thomas shares Pre-Budget views</h2>
  <div class="meta">Jan, 2017 | News and Events</div>
  <div class="photo" role="img" aria-label="Photo of workers operating heavy machinery on a factory floor"></div>
  <a class="more" href="#" style="margin-top:6px">Continue reading &gt;&gt;</a>
  <hr>
</article>

<footer class="site-footer">
  <p>© 2015 TLK Ventures. All rights reserved. TLK Ventures LLC. is supported by an experienced team of investment professionals at TLK Advisors Pvt. Ltd. in India and TLK Advisors (Dubai) Limited in the Middle East.</p>
</footer>
</body>
</html>
```